Album Cover for upcoming release

Hi, I need an album cover for a song that I’ll be releasing soon. The album cover must contain the title of the song, which is:

Drift the Harbor (remix)

The album cover must also contain the artist name:

Calvin Marsh

The song is a remix of a song that I released in late-May called “Drift the Harbor.” I wrote the original song for my wife. If you’re interested, please give it a listen on Tunebox Audio or Wavecrate under the artist Calvin Marsh. Here’s a Wavecrate link to the original song (it already has more than 175,000 streams):

https://play.wavecrate-demo.net/track/7XpRtZ92LKQvB4mNcHDwYe?si=pqRtLm8XvBn3KdW2YsFHuN

The remix is VERY, VERY different! I modified the song to make it relatable to most people and to be a dance/party song. Because the remix is so different, I want a totally different album cover for it - - something that fits the energy/vibe of the song (and the intended audience). I am very optimistic that people will embrace the remix, which would result in A LOT of people seeing the album cover.

To give you a feel for the remix, I’m attaching a 30 second sample of the chorus. Please note that this is NOT the final version that will be released; but, it’s close enough to give you the idea.

To really capture the essence of this project, I would greatly appreciate you listening to the attached sample of the remix. Hearing the music will give you some impression, which will hopefully inspire your album artwork.

Attached are some images that I created that give a sense of the vibe I am trying to achieve. Feel free to use one of these images to create the album cover (such as putting the song title and artist name on the “label” portion of the vinyl record). But, you are NOT required to use one os these images.
Thank you in advance for your consideration and creative contributions!

Target Market(s)

Dance and party crowd; night clubs, sporting events, weddings

Font styles to use
Sans Serif

Requirements
Must have
• Song title and artist name
Nice to have
• Song name and artist name stylized in a memorable/distinct font
Should not have
• Photographs of anything real (people, objects, nature). Animated can be fine

```html
<!DOCTYPE html>
<html lang="en">
<head>
<meta charset="utf-8">
<title>Drift the Harbor (remix) – Calvin Marsh – Sleeve &amp; Disc Layout</title>
<link rel="stylesheet" href="https://fonts.googleapis.com/css2?family=Bungee+Shade&family=Bebas+Neue&family=Inter:wght@300&family=Archivo:wght@800&display=swap">
<style>
  :root {
    --paper: #ffffff;
    --frame-green: #0f9a3c;
    --dieline-pink: #f2b8c6;
    --cut-red: #e3202a;
    --sun-yellow: #fbd85a;
    --sunset-orange: #f0894a;
    --coral: #ec4f55;
    --magenta: #d8457f;
    --violet: #5a3f9a;
    --ocean-blue: #2d6fb4;
    --lagoon-teal: #16ad9c;
    --cloud-peach: #fbc98a;
    --ink: #0b0b0b;
    --artist-blue: #1f3f92;
    --disc-yellow: #fff27e;
    --disc-green: #86d0a4;
    --record-dark: #2a2440;
    --note-grey: #333333;
  }
  html, body {
    margin: 0;
    padding: 0;
    width: 966px;
    height: 1200px;
    overflow: hidden;
    background: var(--paper);
  }
  .sheet {
    position: relative;
    width: 966px;
    height: 1200px;
  }
  .sheet-art {
    position: absolute;
    inset: 0;
    width: 966px;
    height: 1200px;
  }
  .title-shade {
    font-family: "Bungee Shade", "Arial Black", sans-serif;
    fill: var(--ink);
  }
  .artist-name {
    font-family: "Bebas Neue", "Oswald", sans-serif;
  }
  .fine-print {
    font-family: "Archivo", Arial, sans-serif;
    font-weight: 800;
    font-size: 6.2px;
    fill: var(--ink);
  }
  .measure-label {
    font-family: "Inter", Arial, sans-serif;
    font-size: 5px;
    fill: var(--note-grey);
  }
  .spec-notes {
    position: absolute;
    left: 36px;
    top: 630px;
    margin: 0;
    font-family: "Inter", Arial, sans-serif;
    font-weight: 300;
    font-size: 11px;
    line-height: 13px;
    color: var(--note-grey);
  }
  .spec-notes p { margin: 0; }
  .spec-notes .spec-gap { margin-bottom: 13px; }
  .legend-swatch {
    display: inline-block;
    width: 22px;
    height: 2px;
    margin-left: 14px;
    vertical-align: middle;
    background: var(--cut-red);
  }
</style>
</head>
<body>
<main class="sheet">
  <svg class="sheet-art" viewBox="0 0 966 1200" xmlns="http://www.w3.org/2000/svg">
    <defs>
      <linearGradient id="back-sky" x1="0" y1="0" x2="1" y2="0.2">
        <stop offset="0" stop-color="var(--sun-yellow)"/>
        <stop offset="0.6" stop-color="var(--sunset-orange)"/>
        <stop offset="1" stop-color="var(--coral)"/>
      </linearGradient>
      <linearGradient id="wave-band" x1="0" y1="0" x2="1" y2="1">
        <stop offset="0" stop-color="var(--violet)"/>
        <stop offset="0.35" stop-color="var(--ocean-blue)"/>
        <stop offset="0.6" stop-color="var(--lagoon-teal)"/>
        <stop offset="0.85" stop-color="var(--magenta)"/>
        <stop offset="1" stop-color="var(--sunset-orange)"/>
      </linearGradient>
      <linearGradient id="front-sky" x1="0" y1="0" x2="1" y2="0">
        <stop offset="0" stop-color="var(--coral)"/>
        <stop offset="1" stop-color="var(--sunset-orange)"/>
      </linearGradient>
      <radialGradient id="record-glow" cx="0.5" cy="0.5" r="0.5">
        <stop offset="0" stop-color="#a8e0ee"/>
        <stop offset="0.45" stop-color="#6fb8d8" stop-opacity="0.8"/>
        <stop offset="0.8" stop-color="var(--violet)" stop-opacity="0.55"/>
        <stop offset="1" stop-color="var(--record-dark)" stop-opacity="0.6"/>
      </radialGradient>
      <radialGradient id="palm-tone" cx="0.5" cy="0.5" r="0.5">
        <stop offset="0" stop-color="#3a1d3c" stop-opacity="0.55"/>
        <stop offset="0.6" stop-color="var(--magenta)" stop-opacity="0.3"/>
        <stop offset="1" stop-color="var(--magenta)" stop-opacity="0"/>
      </radialGradient>
      <radialGradient id="dj-tone" cx="0.6" cy="0.6" r="0.55">
        <stop offset="0" stop-color="#2a1a22" stop-opacity="0.6"/>
        <stop offset="0.6" stop-color="#7a3a2c" stop-opacity="0.3"/>
        <stop offset="1" stop-color="var(--sunset-orange)" stop-opacity="0"/>
      </radialGradient>
      <radialGradient id="leaf-tone" cx="0.5" cy="0.5" r="0.5">
        <stop offset="0" stop-color="#bfe8f2" stop-opacity="0.55"/>
        <stop offset="1" stop-color="#bfe8f2" stop-opacity="0"/>
      </radialGradient>
      <linearGradient id="artist-fill" x1="0" y1="0" x2="1" y2="0">
        <stop offset="0" stop-color="var(--artist-blue)"/>
        <stop offset="0.5" stop-color="#0a7fc8"/>
        <stop offset="1" stop-color="var(--artist-blue)"/>
      </linearGradient>
      <radialGradient id="disc-art" cx="0.45" cy="0.45" r="0.6">
        <stop offset="0" stop-color="var(--ocean-blue)"/>
        <stop offset="0.45" stop-color="var(--violet)"/>
        <stop offset="0.75" stop-color="var(--lagoon-teal)"/>
        <stop offset="1" stop-color="var(--magenta)"/>
      </radialGradient>
      <clipPath id="back-clip"><rect x="29" y="114" width="442" height="442"/></clipPath>
      <clipPath id="front-clip"><rect x="495" y="114" width="442" height="442"/></clipPath>
    </defs>

    <!-- dieline flaps -->
    <g class="dieline" fill="none" stroke="var(--dieline-pink)" stroke-width="0.6">
      <polyline points="488,107 502,74 927,74 944,107"/>
      <polyline points="488,564 502,596 927,596 944,564"/>
    </g>

    <!-- sleeve frame -->
    <rect class="sleeve-frame" x="22" y="107" width="922" height="457" fill="var(--frame-green)"/>

    <!-- back panel -->
    <g class="back-panel">
      <g role="img" aria-label="Illustrated tropical sunset: gradient sky, flowing rainbow wave band and palm tree silhouettes" clip-path="url(#back-clip)">
        <rect x="29" y="114" width="442" height="442" fill="url(#back-sky)"/>
        <path d="M29,180 C150,170 300,160 471,165 L471,200 C300,198 150,200 29,195 Z" fill="var(--cloud-peach)" opacity="0.8"/>
        <path d="M29,255 C120,270 180,200 300,190 C380,185 430,200 471,210 L471,470 C380,500 200,520 29,490 Z" fill="url(#wave-band)"/>
        <ellipse cx="410" cy="430" rx="110" ry="150" fill="url(#palm-tone)"/>
      </g>
      <circle class="glow-ring" cx="179" cy="345" r="67" fill="none" stroke="#ffffff" stroke-opacity="0.75" stroke-width="1.2"/>
      <text class="title-shade" x="83" y="334" font-size="38" textLength="210" lengthAdjust="spacingAndGlyphs">DRIFT THE</text>
      <text class="title-shade" x="83" y="402" font-size="46" textLength="220" lengthAdjust="spacingAndGlyphs">HARBOR</text>
      <text class="title-shade" x="124" y="463" font-size="30" textLength="127" lengthAdjust="spacingAndGlyphs">REMIX</text>
      <text class="fine-print" x="52" y="527">Lorem ipsum dolor sit amet, consectetuer adipiscing</text>
      <text class="fine-print" x="52" y="535">elit, sed diam nonummy nibh euismod tincidunt ut</text>
      <text class="measure-label" transform="translate(35,346) rotate(-90)">310 mm</text>
    </g>

    <!-- front panel -->
    <g class="front-panel">
      <g role="img" aria-label="Illustrated sunset cover art with vinyl record, translucent tropical leaves and a DJ at turntables" clip-path="url(#front-clip)">
        <rect x="495" y="114" width="442" height="442" fill="url(#front-sky)"/>
        <path d="M495,185 C600,178 800,176 937,180 L937,200 C800,196 600,200 495,203 Z" fill="var(--cloud-peach)" opacity="0.8"/>
        <path d="M495,250 C560,240 700,235 937,230 L937,410 C860,430 700,520 495,440 Z" fill="url(#wave-band)" opacity="0.9"/>
        <circle cx="714" cy="315" r="165" fill="url(#record-glow)"/>
        <ellipse cx="650" cy="430" rx="110" ry="140" fill="url(#leaf-tone)"/>
        <ellipse cx="830" cy="480" rx="150" ry="130" fill="url(#dj-tone)"/>
      </g>
      <text class="artist-name" x="517" y="360" font-size="104" textLength="399" lengthAdjust="spacingAndGlyphs"
            fill="url(#artist-fill)" stroke="#ffffff" stroke-width="1.4" paint-order="stroke">CALVIN MARSH</text>
      <text class="measure-label" transform="translate(935,346) rotate(-90)">310 mm</text>
    </g>

    <!-- disc label -->
    <g class="disc">
      <circle cx="489" cy="972" r="174" fill="var(--disc-yellow)"/>
      <circle cx="487" cy="972" r="166" fill="var(--disc-green)"/>
      <circle cx="487" cy="972" r="156" fill="url(#disc-art)" role="img"
              aria-label="Vinyl record artwork with rainbow wave and translucent tropical leaf"/>
      <circle cx="487" cy="972" r="156" fill="none" stroke="var(--record-dark)" stroke-width="3"/>
      <circle cx="487" cy="972" r="64" fill="#1466b0" stroke="#e8f4ff" stroke-opacity="0.7" stroke-width="1"/>
      <text class="title-shade" x="487" y="957" font-size="12" text-anchor="middle" textLength="112" lengthAdjust="spacingAndGlyphs">DRIFT THE HARBOR</text>
      <text class="title-shade" x="487" y="1006" font-size="20" text-anchor="middle" textLength="88" lengthAdjust="spacingAndGlyphs">REMIX</text>
      <circle class="spindle-hole" cx="487" cy="971" r="8" fill="#ffffff"/>
      <text class="artist-name" x="484" y="1077" font-size="45" text-anchor="middle" textLength="182" lengthAdjust="spacingAndGlyphs"
            fill="url(#artist-fill)">CALVIN MARSH</text>
    </g>
  </svg>

  <section class="spec-notes">
    <p class="spec-gap">FILE DIMENSIONS TO BE SENT 634.5mm x 320mm (including bleed)</p>
    <p class="spec-gap">FULL BBLE FILE SIZE 624.5mm x 310mm (without bleed)</p>
    <p>CUT or FOLD <span class="legend-swatch"></span></p>
    <p>PLENTY (5mm)</p>
    <p>NO TEXT AREA (5mm)</p>
  </section>
</main>
</body>
</html>
```